Solar Business needs infographic for Act Now Campaign

A government solar rebate program is ending and I would like to send out an infographic in an email campaign.

I want to explain with text and graphics why people should ACT NOW! The material has been prepared in Word with Designer Notes at each step of the 7 step infographic. I'd like each step to flow into the next as best it can.

I've prepared the guide in green and would like the infographic in green or the colours of the logo, orange and reds. Key words are highlighted in red, don't need to be in red, just must stand out to the reader.

This is a 'call to action' infographic. Emphasis on ACT NOW with highlights on numbers. Keep the look and feel SIMPLE to highlight the URGENCY and the numbers % and $.

I added a photo of solar on a roof, as an optional extra. I've made a small change to the text/copy of the material in Word.

Deadline approaching. ACT NOW! People who are looking to save electricity costs and install solar

Target Market(s)

35-65
male and female
young couples, retired, working family

Industry/Entity Type

Government

Requirements
Must have
• CALL TO ACTION look and feel. Infographic not limited to one page, scrolling on like a webpage.

Would like to have only two colour themes. Green theme or Red and Orange theme to match the BrelLumo logo.
Nice to have
• Detailed in the brief.

Photo of solar provided as a stock image I own the rights to. Does not have to be used, included as an option.

```html
<!DOCTYPE html>
<html lang="en">
<head>
<meta charset="utf-8">
<title>The Time is Now! – Solar PV</title>
<link rel="stylesheet" href="https://fonts.googleapis.com/css2?family=Rubik:wght@700;800;900&display=swap">
<style>
  :root {
    --green: #3bb54a;
    --white: #ffffff;
    --yellow: #f8ec3a;
    --sky: #4fb6e6;
    --charcoal: #3a4650;
  }
  html, body {
    margin: 0;
    padding: 0;
    overflow: hidden;
  }
  .canvas {
    position: relative;
    width: 728px;
    height: 1200px;
    overflow: hidden;
    background: var(--green);
    font-family: "Rubik", "Arial Rounded MT Bold", sans-serif;
    color: var(--white);
  }
  .headline {
    position: absolute;
    top: 38px;
    left: 0;
    width: 100%;
    margin: 0;
    text-align: center;
    font-size: 70px;
    font-weight: 800;
    letter-spacing: -0.5px;
    line-height: 1;
  }
  .divider {
    position: absolute;
    left: 50px;
    width: 631px;
    height: 3px;
    background: var(--white);
  }
  .divider--top { top: 120px; }
  .divider--mid { top: 322px; }
  .divider--step { top: 778px; }
  .divider--end { top: 968px; }

  .note {
    position: absolute;
    right: 385px;
    margin: 0;
    text-align: right;
    font-size: 20px;
    font-weight: 700;
    line-height: 27.5px;
    white-space: nowrap;
  }
  .note--ret { top: 156px; }
  .note--saving { top: 806px; }

  .urgent {
    position: absolute;
    top: 184px;
    left: 381px;
    width: 300px;
    margin: 0;
    text-align: center;
    line-height: 1;
  }
  .urgent__title {
    display: block;
    color: var(--yellow);
    font-size: 37px;
    font-weight: 800;
  }
  .urgent__sub {
    display: block;
    margin-top: 9px;
    font-size: 28px;
    font-weight: 700;
  }

  .thought-bubbles {
    position: absolute;
    top: 0;
    left: 0;
  }
  .roof-scene {
    position: absolute;
    top: 356px;
    left: 326px;
    width: 330px;
    height: 330px;
    border-radius: 50%;
    background: linear-gradient(180deg, var(--sky) 0%, var(--charcoal) 100%);
  }

  .step-title {
    position: absolute;
    top: 663px;
    left: 52px;
    margin: 0;
    font-size: 48px;
    font-weight: 800;
    line-height: 1;
  }
  .step-title__name { color: var(--yellow); }

  .step-question {
    position: absolute;
    top: 734px;
    left: 0;
    width: 730px;
    margin: 0;
    text-align: center;
    font-size: 31px;
    font-weight: 700;
    line-height: 1;
  }

  .stat {
    position: absolute;
    top: 803px;
    left: 385px;
    width: 300px;
    margin: 0;
    text-align: center;
    font-size: 38px;
    font-weight: 800;
    line-height: 47px;
  }
  .stat__figure { color: var(--yellow); }
</style>
</head>
<body>
<main class="canvas">
  <h1 class="headline">The Time is Now!</h1>
  <div class="divider divider--top"></div>

  <p class="note note--ret">The Federal Government is<br>reviewing the Renewable<br>Energy Target.&nbsp; If the RET<br>goes solar PV cost will<br>increase ~ 30%</p>
  <p class="urgent">
    <span class="urgent__title">LAST CHANCE!</span>
    <span class="urgent__sub">for Solar Rebate</span>
  </p>

  <div class="divider divider--mid"></div>

  <svg class="thought-bubbles" width="728" height="700" viewBox="0 0 728 700" aria-hidden="true">
    <circle cx="278" cy="421" r="36" fill="#ffffff"/>
    <circle cx="197" cy="490" r="29" fill="#ffffff"/>
    <circle cx="208" cy="578" r="20" fill="#ffffff"/>
  </svg>
  <div class="roof-scene" role="img" aria-label="Illustration of solar panels on a house roof under a blue sky with clouds"></div>

  <h2 class="step-title">1. <span class="step-title__name">SOLAR PV</span></h2>
  <p class="step-question">THE SAVING THAT KEEPS ON SAVING?</p>

  <div class="divider divider--step"></div>

  <p class="note note--saving">In Sydney a 5kW system<br>will save you $50k over<br>its lifetime, and that’s<br>excluding inflation.</p>
  <p class="stat">5kWs will Save<br><span class="stat__figure">$50K</span> on<br>electricity bills</p>

  <div class="divider divider--end"></div>
</main>
</body>
</html>
```